Website Design for Business Law Firm

We have a logo and now we would like a web site design for our new website. Our small firm provides creative and aggressive transactional (not litigation) legal services to advise healthcare, technology, internet-based and traditional companies and investors in such companies on healthcare, technology, financing, mergers/acquisitions, real estate and other transactions, legal compliance and general corporate and business matters.

We would like to see a website design that is professional and appropriate for executives, professionals, investors and government regulators to visit, that conveys professionalism and competence while being a little edgy and modern - no typical legal motifs such as gavels, books, or scales of justice. We advise businesses and investors and guide them through complicated issues quickly, capably and differently from other law firms. We are part of the business team and get things done.

The logo is attached, and we like gray as a color to complement it. The intention of the logo is to convey that in a storm or challenging time, people come to this firm, and people come to this firm when they need the power and disruption to change things or shake them up.

I have also enclosed a picture of our business card for consideration.

On the other hand, you can check out the current simple site at www.quenlow.example to see we have used a space motif in the past to evoke that we help create stars (the nebula featured there). This is not a necessary part of the new website and it may look better without it.

We appreciate your creativity and look forward to designs.

Industry/Entity Type

Business

Requirements
Must have
• We anticipate the following pages, and you may submit different ideas for the different pages:
• 1. Landing page
• 2. Services pages - healthcare, IT/Technology, general counsel services, financings, mergers/acquisitions, mediation/arbitration, procurement and productization
• 3. About Us including contact information
• Our name and contact information:
• Quenlow Law Firm, P.C.
• 7816 SW 19th Ave.
• Portland, OR 97213
• phone: 555.614.2873
• fax: 555.730.4158
Nice to have
• Please consider designs that enhance the impressions we are looking for
Should not have
• Please no gavels, scales of justice, law books, or similar traditional legal imagery.

```html
<!DOCTYPE html>
<html lang="en">
<head>
<meta charset="utf-8">
<title>Quenlow Law Firm, P.C.</title>
<link rel="stylesheet" href="https://fonts.googleapis.com/css2?family=Michroma&family=Roboto:wght@300;400&family=Ubuntu:wght@300;400&display=swap">
<style>
:root{
  --hero-dark:#2b3336;
  --hero-mid:#6f8288;
  --hero-light:#a9b8bb;
  --header-band:rgba(140,148,150,.55);
  --panel:rgba(48,50,52,.9);
  --white:#ffffff;
  --ink:#353535;
  --teal:#4d6a72;
  --body-text:#8d8d8d;
  --footer:#85898b;
}
*{margin:0;padding:0;box-sizing:border-box}
html,body{width:1200px;height:982px;overflow:hidden;background:var(--white)}
.page{position:relative;width:1200px;height:982px;font-family:"Ubuntu",sans-serif;color:var(--white)}
.hero-photo{position:absolute;left:0;top:0;width:1200px;height:622px;
  background:linear-gradient(90deg,#4a5558 0%,#7d8d91 18%,var(--hero-dark) 40%,#536268 60%,var(--hero-mid) 80%,#5a6a70 100%),var(--hero-dark);
  background-blend-mode:normal}
.hero-photo::after{content:"";position:absolute;inset:0;background:linear-gradient(180deg,rgba(169,184,187,.25),rgba(0,0,0,.15) 70%,rgba(0,0,0,.3))}
.header-band{position:absolute;left:0;top:0;width:1200px;height:111px;background:var(--header-band)}
.brand{position:absolute;left:206px;top:14px;width:290px;text-align:center;font-family:"Michroma",sans-serif;color:var(--white)}
.brand-name{display:block;font-size:34px;letter-spacing:9px;line-height:60px}
.brand-sub{display:block;font-size:15px;letter-spacing:4px;margin-top:6px}
.contact-top{position:absolute;right:192px;top:20px;text-align:right;font-family:"Michroma",sans-serif;font-size:13px;letter-spacing:3px;line-height:28px}
.contact-top svg{vertical-align:-3px;margin-right:10px}
.account-links{position:absolute;right:191px;top:79px;font-size:15px;font-family:"Ubuntu",sans-serif}
.account-links a{color:var(--white);text-decoration:none;margin-left:14px}
.headline{position:absolute;left:0;top:166px;width:1194px;text-align:center;font-family:"Roboto",sans-serif;font-weight:300;font-size:42px;line-height:47px;letter-spacing:-.5px}
.services{position:absolute;left:190px;top:310px;width:818px;height:258px;background:var(--panel)}
.service-col{position:absolute;top:18px;list-style:none}
.service-col li{position:relative;padding-left:29px;font-size:15px;line-height:22px;margin-bottom:15px;font-weight:300}
.service-col li svg{position:absolute;left:0;top:0}
.col-a{left:32px}.col-b{left:326px;width:200px}.col-c{left:550px;width:260px}
.welcome{position:absolute;left:0;top:622px;width:1200px;height:250px;background:var(--white)}
.welcome::before{content:"";position:absolute;left:200px;right:200px;top:0;height:14px;background:radial-gradient(ellipse at top,rgba(0,0,0,.18),transparent 70%)}
.welcome-title{position:absolute;left:0;top:34px;width:1194px;text-align:center;font-family:"Michroma",sans-serif;font-weight:400;font-size:21px;letter-spacing:5px;color:var(--ink)}
.welcome-title span{color:var(--teal)}
.welcome-text{position:absolute;left:206px;top:84px;width:480px;font-family:"Roboto",sans-serif;font-weight:300;font-size:13.5px;line-height:20.3px;color:var(--body-text)}
.team-photo{position:absolute;left:742px;top:88px;width:258px;height:131px;background:linear-gradient(90deg,#5a3418,#8a5a30 40%,#6a3e1e 75%,#3a2418)}
.footer{position:absolute;left:0;top:872px;width:1200px;height:110px;background:linear-gradient(180deg,#6e7274,var(--footer) 50%,#7a7e80)}
.copyright{position:absolute;left:200px;top:28px;font-size:13px}
.email{position:absolute;left:200px;top:58px;font-size:16px}
.address{position:absolute;left:600px;top:26px;font-size:16px}
.phones{position:absolute;left:600px;top:58px;font-size:16px}
.footer svg{vertical-align:-3px;margin-right:10px}
.phones .fax{margin-left:16px}
</style>
</head>
<body>
<div class="page">
  <div class="hero-photo" role="img" aria-label="Blurred photograph of a library aisle with shelved volumes, tinted blue-grey"></div>
  <header class="header-band">
    <div class="brand"><span class="brand-name">QUENLOW</span><span class="brand-sub">LAW FIRM</span></div>
    <div class="contact-top">
      <div><svg width="16" height="14" viewBox="0 0 16 14"><path d="M1 5c0-3 14-3 14 0v2h-4V5H5v2H1z M3 8h10l1 5H2z" fill="#fff"/></svg>TEL: 555.614.2873</div>
      <div><svg width="16" height="14" viewBox="0 0 16 14"><rect x="4" y="1" width="8" height="4" fill="#fff"/><rect x="1" y="5" width="14" height="5" rx="1" fill="#fff"/><rect x="4" y="10" width="8" height="3" fill="#fff"/></svg>FAX: 555.730.4158</div>
    </div>
    <nav class="account-links"><a href="#">For lawyers</a><a href="#">Sign in</a><a href="#">Register</a></nav>
  </header>
  <h1 class="headline">PRAGMATIC,CREATIVE SERVICES<br>FOR INNOVATIVE BUSINESSES</h1>
  <section class="services">
    <ul class="service-col col-a">
      <li><svg width="22" height="22" viewBox="0 0 22 22"><circle cx="11" cy="11" r="10" fill="none" stroke="#fff" stroke-width="1.5"/><path d="M9 6.5l4.5 4.5L9 15.5" fill="none" stroke="#fff" stroke-width="2"/></svg>Outsourcing</li>
      <li><svg width="22" height="22" viewBox="0 0 22 22"><circle cx="11" cy="11" r="10" fill="none" stroke="#fff" stroke-width="1.5"/><path d="M9 6.5l4.5 4.5L9 15.5" fill="none" stroke="#fff" stroke-width="2"/></svg>Venture Financing</li>
      <li><svg width="22" height="22" viewBox="0 0 22 22"><circle cx="11" cy="11" r="10" fill="none" stroke="#fff" stroke-width="1.5"/><path d="M9 6.5l4.5 4.5L9 15.5" fill="none" stroke="#fff" stroke-width="2"/></svg>Stragtegic Alliances</li>
      <li><svg width="22" height="22" viewBox="0 0 22 22"><circle cx="11" cy="11" r="10" fill="none" stroke="#fff" stroke-width="1.5"/><path d="M9 6.5l4.5 4.5L9 15.5" fill="none" stroke="#fff" stroke-width="2"/></svg>Procurements-Buying or selling</li>
      <li><svg width="22" height="22" viewBox="0 0 22 22"><circle cx="11" cy="11" r="10" fill="none" stroke="#fff" stroke-width="1.5"/><path d="M9 6.5l4.5 4.5L9 15.5" fill="none" stroke="#fff" stroke-width="2"/></svg>Venture Formation and startup</li>
      <li><svg width="22" height="22" viewBox="0 0 22 22"><circle cx="11" cy="11" r="10" fill="none" stroke="#fff" stroke-width="1.5"/><path d="M9 6.5l4.5 4.5L9 15.5" fill="none" stroke="#fff" stroke-width="2"/></svg>Licensing and Technology Exploitation</li>
    </ul>
    <ul class="service-col col-b">
      <li><svg width="22" height="22" viewBox="0 0 22 22"><circle cx="11" cy="11" r="10" fill="none" stroke="#fff" stroke-width="1.5"/><path d="M9 6.5l4.5 4.5L9 15.5" fill="none" stroke="#fff" stroke-width="2"/></svg>Contracts</li>
      <li><svg width="22" height="22" viewBox="0 0 22 22"><circle cx="11" cy="11" r="10" fill="none" stroke="#fff" stroke-width="1.5"/><path d="M9 6.5l4.5 4.5L9 15.5" fill="none" stroke="#fff" stroke-width="2"/></svg>Real Estate</li>
      <li><svg width="22" height="22" viewBox="0 0 22 22"><circle cx="11" cy="11" r="10" fill="none" stroke="#fff" stroke-width="1.5"/><path d="M9 6.5l4.5 4.5L9 15.5" fill="none" stroke="#fff" stroke-width="2"/></svg>Dispute Resolution</li>
      <li><svg width="22" height="22" viewBox="0 0 22 22"><circle cx="11" cy="11" r="10" fill="none" stroke="#fff" stroke-width="1.5"/><path d="M9 6.5l4.5 4.5L9 15.5" fill="none" stroke="#fff" stroke-width="2"/></svg>Audits,Analyses and legal project management</li>
      <li><svg width="22" height="22" viewBox="0 0 22 22"><circle cx="11" cy="11" r="10" fill="none" stroke="#fff" stroke-width="1.5"/><path d="M9 6.5l4.5 4.5L9 15.5" fill="none" stroke="#fff" stroke-width="2"/></svg>Creative Private Financing Arrangements</li>
    </ul>
    <ul class="service-col col-c">
      <li><svg width="22" height="22" viewBox="0 0 22 22"><circle cx="11" cy="11" r="10" fill="none" stroke="#fff" stroke-width="1.5"/><path d="M9 6.5l4.5 4.5L9 15.5" fill="none" stroke="#fff" stroke-width="2"/></svg>Mergers and Acquisitions</li>
      <li><svg width="22" height="22" viewBox="0 0 22 22"><circle cx="11" cy="11" r="10" fill="none" stroke="#fff" stroke-width="1.5"/><path d="M9 6.5l4.5 4.5L9 15.5" fill="none" stroke="#fff" stroke-width="2"/></svg>Businesses Relationships</li>
      <li><svg width="22" height="22" viewBox="0 0 22 22"><circle cx="11" cy="11" r="10" fill="none" stroke="#fff" stroke-width="1.5"/><path d="M9 6.5l4.5 4.5L9 15.5" fill="none" stroke="#fff" stroke-width="2"/></svg>Service as a Mediator or Arbitrator</li>
      <li><svg width="22" height="22" viewBox="0 0 22 22"><circle cx="11" cy="11" r="10" fill="none" stroke="#fff" stroke-width="1.5"/><path d="M9 6.5l4.5 4.5L9 15.5" fill="none" stroke="#fff" stroke-width="2"/></svg>Vandor Management</li>
      <li><svg width="22" height="22" viewBox="0 0 22 22"><circle cx="11" cy="11" r="10" fill="none" stroke="#fff" stroke-width="1.5"/><path d="M9 6.5l4.5 4.5L9 15.5" fill="none" stroke="#fff" stroke-width="2"/></svg>Local Counsel for Transactions and dueDiligence</li>
    </ul>
  </section>
  <section class="welcome">
    <h2 class="welcome-title">WELLCOME TO <span>QUENLOW LAW FIRM,P.C</span></h2>
    <p class="welcome-text">Lorem ipsum dolor sit amet, consectetuer adipiscing elit, sed diam nonummy nibh euismod tincidunt ut laoreet dolore magna aliquam erat volutpat. Ut wisi enim ad minim veniam, quis nostrud exerci tation ullamcorper suscipit lobortis nisl ut aliquip ex ea commodo consequat. Duis autem vel eum iriure dolor in hendrerit in vulputate velit esse molestie consequat, vel illum dolore eu feugiat nulla facilisis at vero eros et accumsan et iusto odio dignissim qui blandit praesent luptatum zzril delenit augue duis dolore te feugait nulla facilisi.</p>
    <div class="team-photo" role="img" aria-label="Photograph of an attorney in a suit meeting with a client in a wood-panelled office"></div>
  </section>
  <footer class="footer">
    <div class="copyright">Copyright © 2013 Quenlow Law Firm,p.c All rights reserved.</div>
    <div class="email"><svg width="20" height="14" viewBox="0 0 20 14"><rect x="1" y="1" width="18" height="12" fill="none" stroke="#fff" stroke-width="1.5"/><path d="M1 1l9 7 9-7" fill="none" stroke="#fff" stroke-width="1.5"/></svg>info@quenlow.example</div>
    <div class="address"><svg width="18" height="22" viewBox="0 0 18 22"><path d="M9 1a7 7 0 0 0-7 7c0 5 7 13 7 13s7-8 7-13a7 7 0 0 0-7-7z" fill="none" stroke="#fff" stroke-width="1.5"/><circle cx="9" cy="8" r="2.5" fill="#fff"/></svg>Quenlow Law Firm,p.c &nbsp;P.O.Box 6152,Portland,or 97208</div>
    <div class="phones"><svg width="16" height="14" viewBox="0 0 16 14"><path d="M1 5c0-3 14-3 14 0v2h-4V5H5v2H1z M3 8h10l1 5H2z" fill="#fff"/></svg>Tel: 555.614.2873<span class="fax"><svg width="16" height="14" viewBox="0 0 16 14"><rect x="4" y="1" width="8" height="4" fill="#fff"/><rect x="1" y="5" width="14" height="5" rx="1" fill="#fff"/><rect x="4" y="10" width="8" height="3" fill="#fff"/></svg>fax: 555.730.4158</span></div>
  </footer>
</div>
</body>
</html>
```